Body therapist needs a business card

I need a card for my business which is teaching trainings in body therapy, the company is called Wexcombe Educational Group. I teach to massage therapists around Australia, South East Asia and the USA. I am attaching my logo which will guide you as to what colours I would like to have you consider. Please consult my website to find out more about what I do. www.corvantela.com.au

My name is Daniel Wexcombe. My phone number is (03) 9417 2608 or 0461753208. email is info@corvantela.com.au

```html
<!DOCTYPE html>
<html lang="en">
<head>
<meta charset="utf-8">
<title>Wexcombe Educational Group – Business Card</title>
<link href="https://fonts.googleapis.com/css2?family=Open+Sans:wght@400;600;700&display=swap" rel="stylesheet">
<style>
  :root {
    --page-bg: #e6e4e1;
    --card-white: #ffffff;
    --brown-deep: #5a3220;
    --brown-warm: #8e4d1f;
    --lime: #c9d92e;
    --red: #b42025;
    --text-dark: #3b2a22;
    --text-soft: #4a4a4a;
  }
  * { margin: 0; padding: 0; box-sizing: border-box; }
  html, body {
    width: 1200px;
    height: 714px;
    overflow: hidden;
    background: var(--page-bg);
    font-family: "Open Sans", Arial, sans-serif;
  }
  .canvas {
    position: relative;
    width: 1200px;
    height: 714px;
  }
  .card {
    position: absolute;
    top: 197px;
    width: 560px;
    height: 320px;
    overflow: hidden;
    box-shadow: 0 3px 10px rgba(0,0,0,0.25);
  }
  .card-front { left: 34px; background: var(--card-white); }
  .card-back  { left: 606px; background: var(--brown-deep); }

  .card-art {
    position: absolute;
    inset: 0;
    width: 560px;
    height: 320px;
  }

  .brand-name {
    position: absolute;
    left: 27px;
    top: 48px;
    font-size: 17px;
    font-weight: 400;
    color: var(--brown-deep);
    letter-spacing: 0.2px;
  }
  .brand-dot {
    position: absolute;
    left: 27px;
    top: 26px;
    width: 16px;
    height: 16px;
    border-radius: 50%;
    background: var(--lime);
  }
  .holder-name {
    position: absolute;
    left: 24px;
    top: 133px;
    font-size: 20px;
    font-weight: 700;
    color: var(--brown-deep);
  }
  .contact-list {
    position: absolute;
    left: 25px;
    top: 184px;
    list-style: none;
    font-size: 15px;
    color: var(--text-dark);
  }
  .contact-list li {
    display: flex;
    align-items: center;
    height: 21.5px;
  }
  .contact-list svg {
    width: 12px;
    height: 12px;
    margin-right: 3px;
    flex: none;
  }
  .regions {
    position: absolute;
    left: 26px;
    top: 265px;
    font-size: 15px;
    color: var(--text-soft);
  }

  .back-title {
    position: absolute;
    left: 210px;
    top: 186px;
    font-size: 45px;
    font-weight: 400;
    color: var(--card-white);
    line-height: 1;
  }
  .back-subtitle {
    position: absolute;
    left: 212px;
    top: 246px;
    font-size: 19px;
    font-weight: 400;
    color: var(--card-white);
  }
</style>
</head>
<body>
<main class="canvas">

  <section class="card card-front" aria-label="Business card front">
    <svg class="card-art" viewBox="0 0 560 320" aria-hidden="true">
      <circle cx="517" cy="154" r="118" fill="var(--brown-warm)"/>
    </svg>

    <span class="brand-dot" aria-hidden="true"></span>
    <p class="brand-name">Wexcombe Educational Group</p>

    <h1 class="holder-name">Daniel Wexcombe</h1>

    <ul class="contact-list">
      <li>
        <svg viewBox="0 0 12 12" aria-hidden="true"><path d="M2.5 1 L4.5 3.4 L3.4 4.6 C4.1 6.1 5.6 7.6 7.1 8.3 L8.3 7.2 L10.8 9.2 L9.6 10.9 C5.5 10.6 1.2 6.3 0.9 2.2 Z" fill="var(--lime)"/></svg>
        (03) 9417 2608
      </li>
      <li>
        <svg viewBox="0 0 12 12" aria-hidden="true"><rect x="1" y="3" width="10" height="7" fill="var(--lime)"/><path d="M1 3 L6 7 L11 3" stroke="#fff" stroke-width="1" fill="none"/></svg>
        info@corvantela.com.au
      </li>
      <li>
        <svg viewBox="0 0 12 12" aria-hidden="true"><circle cx="6" cy="6.5" r="4.8" fill="var(--lime)"/><path d="M1.2 6.5 H10.8 M6 1.7 C3.8 4 3.8 9 6 11.3 M6 1.7 C8.2 4 8.2 9 6 11.3" stroke="#fff" stroke-width="0.8" fill="none"/></svg>
        www.corvantela.com.au
      </li>
    </ul>

    <p class="regions">Australia | South East Asia | USA</p>
  </section>

  <section class="card card-back" aria-label="Business card back">
    <svg class="card-art" viewBox="0 0 560 320" aria-hidden="true">
      <circle cx="93" cy="77" r="78" fill="var(--lime)"/>
    </svg>
    <p class="back-title">Wexcombe</p>
    <p class="back-subtitle">Educational Group</p>
  </section>

</main>
</body>
</html>
```